Flyer for Clothing Line Launch Event

I need a flyer designed for the launch of my women's clothing line in February 2016. I will need to use this flyer on my website, social media and print.

The Collections

Our contemporary collections are comprised of influences drawing from bohemian and chic motifs. The term "Bohemian" is described as "simply an artist or littérateur who, consciously or unconsciously, secedes from conventionality in life and in art". "Chic" was borrowed from the French in the late 19th century and has come to mean stylish or elegant.

About my company:

We design free and romantic garments targeted to fashion-forward women driven by uniqueness and desire to accentuate her confidence and class through style. We look forward to our clients indulging in the LorettaVance brand to include our Keystone Circle, Lend-A-Heart, eNewsletters, Trunk Shows and Fashion Shows.

Target Market(s)

upscale women ages 30-50

Industry/Entity Type

Fashion

Font styles to use
Decorative
Script
Other font styles liked:
• Handwritten type script

Colors
000000
f37122
3377b5
e667a6

Requirements
Must have
• colors similar to my website boutique.lorettavance-example.com
• my logo
Nice to have
• image from my website
• my logo

```html
<!DOCTYPE html>
<html lang="en">
<head>
<meta charset="utf-8">
<title>LorettaVance Boutique — Collection Launch Soiree</title>
<link rel="stylesheet" href="https://fonts.googleapis.com/css2?family=Gelasio:wght@400;700&family=Allura&family=Courier+Prime&display=swap">
<style>
  :root {
    --ink-blue: #2f5f8a;
    --ink-black: #111111;
    --accent-orange: #e07a2e;
    --event-red: #7a2418;
    --bg-gold: #d9cd9c;
    --bg-cream: #ebe8dd;
    --bg-slate: #a9bcc0;
    --edge-mist: #f4f6f7;
    --photo-skin: #b98a5e;
    --photo-gold: #c9a35a;
    --photo-teal: #1f6a72;
  }
  * { margin: 0; padding: 0; box-sizing: border-box; }
  html, body { width: 1200px; height: 2240px; overflow: hidden; }
  body { background: var(--edge-mist); }

  .flyer {
    position: relative;
    width: 1200px;
    height: 2240px;
    overflow: hidden;
    background:
      linear-gradient(90deg,
        var(--edge-mist) 0%, rgba(200,205,210,0.55) 6%, rgba(255,255,255,0.9) 11%,
        rgba(255,255,255,0) 26%, rgba(255,255,255,0) 74%,
        rgba(255,255,255,0.9) 89%, rgba(200,205,210,0.55) 94%, var(--edge-mist) 100%),
      linear-gradient(180deg,
        var(--bg-gold) 0%, #e2dbbd 14%, var(--bg-cream) 36%, #e0e1da 60%, var(--bg-slate) 82%, #8fa8ae 100%);
  }

  .headline {
    position: absolute; top: 262px; left: 0; width: 100%;
    text-align: center;
    font-family: "Gelasio", serif; font-weight: 700;
    font-size: 76px; color: var(--ink-blue);
  }

  .boutique-name {
    position: absolute; top: 430px; left: 0; width: 100%;
    text-align: center; white-space: nowrap;
  }
  .boutique-name .script {
    font-family: "Allura", cursive; font-size: 124px; color: var(--ink-black);
  }
  .boutique-name .word {
    font-family: "Gelasio", serif; font-size: 56px; color: var(--ink-blue);
    margin-left: 14px;
  }

  .invitation {
    position: absolute; top: 600px; left: 0; width: 100%;
    text-align: center;
    font-family: "Gelasio", serif; font-size: 38px; line-height: 46px;
    color: var(--ink-blue);
  }

  .event-date {
    position: absolute; top: 742px; left: 0; width: 100%;
    text-align: center;
    font-family: "Gelasio", serif; font-size: 42px; color: var(--accent-orange);
  }

  .brand-mark {
    position: absolute; top: 1030px; left: 0; width: 100%;
    display: flex; flex-direction: column; align-items: center; gap: 44px;
  }
  .brand-mark .dot {
    width: 130px; height: 130px; border-radius: 50%;
    background: var(--ink-blue);
  }
  .brand-mark .name {
    font-family: "Gelasio", serif; font-weight: 400;
    font-size: 66px; color: var(--ink-blue);
  }

  .highlights {
    position: absolute; top: 1562px; left: 0; width: 100%;
    list-style: none; text-align: center;
    font-family: "Courier Prime", monospace; font-size: 40px; line-height: 52px;
    color: var(--event-red);
  }

  .campaign-photo {
    position: absolute; left: 0; bottom: 0; width: 1200px; height: 392px;
    background:
      linear-gradient(90deg, rgba(90,55,30,0.9) 0%, rgba(185,138,94,0.2) 22%, rgba(0,0,0,0) 40%),
      linear-gradient(90deg, var(--photo-skin) 0%, var(--photo-gold) 35%, #a07a3c 58%, var(--photo-teal) 80%, #174e57 100%);
  }
</style>
</head>
<body>
<main class="flyer">
  <h1 class="headline">Introducing</h1>

  <div class="boutique-name">
    <span class="script">LorettaVance</span><span class="word">Boutique</span>
  </div>

  <p class="invitation">
    Please join<br>
    Designer LorettaVance<br>
    For her Collection Launch Soiree
  </p>

  <p class="event-date">February 20, 2016</p>

  <div class="brand-mark">
    <span class="dot"></span>
    <span class="name">LorettaVance</span>
  </div>

  <ul class="highlights">
    <li>Runway Show</li>
    <li>Shopping</li>
    <li>Lite Bites &amp; Champaign</li>
  </ul>

  <div class="campaign-photo" role="img" aria-label="Fashion photograph of a model with long auburn hair reclining in a gold bohemian gown against a teal backdrop"></div>
</main>
</body>
</html>
```